Business Card Design Project

I need a new business card design for my building/development company: Kestrel Ridge Builders.

We specialise in small sub-divisions, multi-story developments and new house builds.
We handle the whole process from concept stage right throught to a fully developed property.
Updates

Target Market(s)

people looking to develop their property and need help. New property buyers

Industry/Entity Type

House

Requirements
Must have
• My logo on both sides:
Side 1: Logo taking up whole side as per old card but with a color/style change.

Side 2: Contact page: include logo but the rest just surprise me!

All contact details will be: (and need to be changable for each employee) I'll inform you of specifics before printing.

Name Surname
Position ie. Managing director
M: insert mobile
E: insert email
P.O. Box 518, Ashwell, Vic, 3094
www.kestrelridgebuilders.com.au

Nice to have
• Colors i'd like: (not necessarily all but this is the basic idea)

Black, blue, grey, silver, white

```html
<!DOCTYPE html>
<html lang="en">
<head>
<meta charset="utf-8">
<title>Kestrel Ridge Builders – Business Card</title>
<link rel="stylesheet" href="https://fonts.googleapis.com/css2?family=Arimo:wght@700&family=Open+Sans:wght@400;600;700&display=swap">
<style>
  :root {
    --page: #ffffff;
    --ink: #000000;
    --card: #000000;
    --glow: #ffffff;
    --glow-edge: #cfcfcf;
    --brand-blue: #1b8fd8;
    --tagline: #111111;
    --contact-text: #ffffff;
  }
  * { box-sizing: border-box; margin: 0; padding: 0; }
  html, body {
    width: 1200px;
    height: 601px;
    overflow: hidden;
    background: var(--page);
  }
  .sheet {
    position: relative;
    width: 1200px;
    height: 601px;
  }
  .sheet-title {
    position: absolute;
    left: 0;
    width: 1272px;
    top: 76px;
    text-align: center;
    font-family: "Arimo", Arial, sans-serif;
    font-weight: 700;
    font-size: 68px;
    line-height: 80px;
    color: var(--ink);
  }
  .card {
    position: absolute;
    top: 216px;
    width: 556px;
    height: 309px;
    overflow: hidden;
    background: var(--card);
    font-family: "Open Sans", Arial, sans-serif;
  }
  .card--front {
    left: 16px;
    background:
      radial-gradient(circle 232px at 274px 152px,
        var(--glow) 0, var(--glow) 58%, #eeeeee 74%, var(--glow-edge) 88%, #3a3a3a 97%, var(--card) 100%);
  }
  .card--back {
    left: 616px;
    background:
      radial-gradient(circle 220px at 128px 60px,
        var(--glow) 0, var(--glow) 55%, #eeeeee 72%, var(--glow-edge) 88%, #3a3a3a 97%, var(--card) 100%);
  }
  .brand-mark {
    position: absolute;
    background: var(--brand-blue);
  }
  .card--front .brand-mark {
    left: 230px;
    top: 56px;
    width: 90px;
    height: 90px;
  }
  .card--back .brand-mark {
    left: 98px;
    top: 34px;
    width: 56px;
    height: 56px;
  }
  .brand-name {
    position: absolute;
    font-weight: 600;
    color: var(--brand-blue);
    white-space: nowrap;
    line-height: 1;
  }
  .brand-tagline {
    position: absolute;
    color: var(--tagline);
    white-space: nowrap;
    line-height: 1;
  }
  .card--front .brand-name {
    left: 0;
    width: 548px;
    top: 176px;
    text-align: center;
    font-size: 36px;
  }
  .card--front .brand-tagline {
    left: 0;
    width: 548px;
    top: 220px;
    text-align: center;
    font-size: 17px;
    letter-spacing: 0.3px;
  }
  .card--back .brand-name {
    left: 16px;
    top: 110px;
    font-size: 23px;
  }
  .card--back .brand-tagline {
    left: 27px;
    top: 136px;
    font-size: 11.5px;
    letter-spacing: 0.2px;
  }
  .contact {
    position: absolute;
    left: 295px;
    top: 126px;
    color: var(--contact-text);
    font-size: 15px;
    line-height: 21px;
    white-space: nowrap;
  }
  .contact-name {
    font-weight: 700;
    font-size: 25px;
    line-height: 30px;
    margin: 0 0 14px 31px;
  }
</style>
</head>
<body>
  <main class="sheet">
    <h1 class="sheet-title">Business Card</h1>

    <section class="card card--front" aria-label="Card front">
      <span class="brand-mark" aria-hidden="true"></span>
      <p class="brand-name">Kestrel Ridge Builders</p>
      <p class="brand-tagline">renovation-construction-development</p>
    </section>

    <section class="card card--back" aria-label="Card back">
      <span class="brand-mark" aria-hidden="true"></span>
      <p class="brand-name">Kestrel Ridge Builders</p>
      <p class="brand-tagline">renovation-construction-development</p>
      <div class="contact">
        <p class="contact-name">Marcus Delane</p>
        <p class="contact-line">Position ie. Managing director</p>
        <p class="contact-line">M: 0412 555 207</p>
        <p class="contact-line">E: kestrelridge@mailhub.com.au</p>
        <p class="contact-line">P.O. Box 518, Ashwell, Vic, 3094</p>
        <p class="contact-line">www.kestrelridgebuilders.com.au</p>
      </div>
    </section>
  </main>
</body>
</html>
```